Skincare Product Packaging Box Design

bright harbor skincare is launching an acne kit to help clear people's skin. The shipping box needs to communicate our brand values and look amazing. We intend on using this acne kit as a subscription service for acne treatment. The shipping box size is 10 x 6 x 3. We have a dieline template for the box, but first we'd like to see your design idea overlaid on the 3 dimensional box, then if we choose your design that would need to be put on the dieline template.

As far as the colors we'd like to use - we should have some elements of the colors of our brand, but feel free to try other colors as well.

Target Market(s)

All ages, ethnicities and genders. Basically anyone with acne.

Industry/Entity Type

Skin Care Product

Font styles to use
Sans Serif

Requirements
Must have
• 1. Design must be gender neutral.
2. We want irregular shapes of color on the box.
3. We need "acne kit" written to describe the box.
4. Must have the bright harbor logo (please take the logo off of file #10).
5. Use the colors for the box design from the first file titled "use these colors".
6. Use the 3 dimensional box image to represent your idea
Nice to have
• vibrant, no pics of acne, try to focus on appealing to all races and genders. Focus on images of the products with vibrant colors in the background. We are not sure if we want images of our products to be included on the box or not. I have attached images of our products so that you have an idea of our branding. But the attached products are not the actual ones that will be going into the kit.
Should not have
• No lotus flowers. No stock images of super attractive women with cream on their face and cucumbers. No cheesy stock images of an outline of a face.

```html
<!DOCTYPE html>
<html lang="en">
<head>
<meta charset="utf-8">
<title>bright harbor skincare – Acne Kit shipping box dieline</title>
<link rel="stylesheet" href="https://fonts.googleapis.com/css2?family=Oswald:wght@500;600&family=Roboto+Condensed:wght@400;700&display=swap">
<style>
  :root {
    --page: #f7f8fa;
    --sage: #b0bfbe;
    --teal: #739c96;
    --brown: #3e342c;
    --orange: #ef7d22;
    --forest: #0f4f45;
    --mist: #d4e2e8;
    --fold: #7d7f80;
    --white: #ffffff;
  }
  html, body {
    margin: 0;
    width: 676px;
    height: 1200px;
    overflow: hidden;
    background: var(--page);
  }
  .canvas {
    width: 676px;
    height: 1200px;
    display: flex;
    align-items: center;
    justify-content: center;
  }
  .dieline { display: block; }
  .panel-bg { fill: var(--sage); }
  .blob-teal { fill: var(--teal); }
  .blob-brown { fill: var(--brown); }
  .blob-orange { fill: var(--orange); }
  .pattern-dots { fill: var(--mist); opacity: 0.45; }
  .pattern-contour { fill: var(--white); opacity: 0.18; }
  .fold-line { fill: none; stroke: var(--fold); stroke-width: 2.5; }
  .brand-name {
    font-family: "Oswald", sans-serif;
    font-weight: 600;
    fill: var(--brown);
  }
  .label-badge { fill: var(--forest); }
  .label-text {
    font-family: "Oswald", sans-serif;
    font-weight: 500;
    fill: var(--white);
    font-size: 44px;
  }
  .ingredients {
    font-family: "Roboto Condensed", sans-serif;
    font-size: 9px;
    fill: var(--brown);
  }
  .ingredients .claims { font-weight: 700; }
</style>
</head>
<body>
<main class="canvas">
  <svg class="dieline" width="640" height="719" viewBox="0 0 930 1045" xmlns="http://www.w3.org/2000/svg" aria-label="Acne Kit shipping box dieline, flat">
    <rect class="panel-bg" x="0" y="0" width="930" height="1045"/>

    <!-- colour blobs -->
    <path class="blob-teal" d="M0,0 H470 C520,60 400,110 300,115 C230,120 215,200 228,260 C240,315 150,330 90,320 C40,312 0,300 0,300 Z"/>
    <path class="blob-brown" d="M450,0 H930 V300 C880,292 840,265 785,245 C762,165 752,112 700,102 C620,92 540,112 490,62 Z"/>
    <path class="blob-orange" d="M0,358 C130,340 320,430 400,525 C320,615 130,700 0,695 Z"/>
    <path class="blob-teal" d="M0,735 C80,712 180,730 200,800 C230,900 300,965 420,1045 H0 Z"/>
    <path class="blob-brown" d="M930,778 C860,768 795,790 762,842 C722,920 640,958 480,980 C448,992 440,1022 458,1045 H930 Z"/>

    <!-- decorative pattern areas -->
    <path class="pattern-dots" role="img" aria-label="Scattered light blue dot pattern" d="M640,360 C700,330 760,290 930,280 V770 C860,765 800,720 760,680 C720,640 650,600 640,560 Z"/>
    <path class="pattern-contour" role="img" aria-label="White contour line ornament" d="M160,255 C230,240 260,330 250,420 C240,500 270,580 255,680 C245,770 205,800 160,790 C110,780 100,700 110,620 C120,540 95,460 105,380 C112,310 120,265 160,255 Z"/>

    <!-- ingredients, printed upside down on the inner flap -->
    <g class="ingredients" transform="rotate(180 460 210)">
      <text x="215" y="150" textLength="485">INGREDIENTS: Aqua, Orange Flower Water, Glycerin, Betaine, Aloe Leaf Juice, Green Tea Extract,</text>
      <text x="215" y="164" textLength="485">Rosehip Seed Oil, Tea Tree Oil, Willow Bark Extract, Licorice Root Extract, Calendula Extract,</text>
      <text x="215" y="178" textLength="485">Vitamin C, Niacinamide, Zinc PCA, Sea Buckthorn Oil, Jojoba Oil, Chamomile Extract, Panthenol,</text>
      <text x="215" y="192">Xanthan Gum, Sodium Hydroxide, Phenoxyethanol, Ethylhexylglycerin.</text>
      <text class="claims" x="215" y="208">VEGAN, CRUELTY AND PARABEN FREE    BRIGHTHARBORSKINCARE.COM</text>
    </g>

    <!-- side panel brand -->
    <text class="brand-name" x="640" y="472" font-size="40" textLength="180" lengthAdjust="spacingAndGlyphs">bright harbor</text>

    <!-- top panel brand -->
    <text class="brand-name" x="293" y="770" font-size="84" textLength="345" lengthAdjust="spacingAndGlyphs">bright harbor</text>

    <!-- product label -->
    <rect class="label-badge" x="380" y="874" width="170" height="92" rx="6"/>
    <text class="label-text" x="465" y="936" text-anchor="middle">ACNE KIT</text>

    <!-- fold and cut lines -->
    <rect class="fold-line" x="1.5" y="1.5" width="927" height="1042"/>
    <line class="fold-line" x1="175" y1="0" x2="175" y2="1045"/>
    <line class="fold-line" x1="755" y1="0" x2="755" y2="1045"/>
    <line class="fold-line" x1="0" y1="350" x2="930" y2="350"/>
    <line class="fold-line" x1="0" y1="525" x2="930" y2="525"/>
    <line class="fold-line" x1="0" y1="872" x2="930" y2="872"/>
  </svg>
</main>
</body>
</html>
```